Letterhead and Envelopes design using existing logo. Logo can be found at tqvanholt.com

Use existing logo (attached) and incorporate in letterhead and envelope designs.

Current logo can be viewed at tqvanholt.com the web site reflect various parent and sub companies. Please see attached as well.

Target Market(s)

Other oil and gas operators.

Industry/Entity Type

Oil And Gas

Font styles to use
Sans Serif

Colors

Designer to choose colors to be used in the design.

Requirements
Must have
• Current logo and address
Nice to have
• Modern, contemporary approach yet incorporate existing traditional design.
• After design is selected for Wexford Tiller Holdings I will use similar design for Royalties, Exploration, Energy and Farms with different color schemes.

```html
<!DOCTYPE html>
<html lang="en">
<head>
<meta charset="UTF-8">
<title>Wexford Tiller Holdings — Letterhead</title>
<link rel="stylesheet" href="https://fonts.googleapis.com/css2?family=Montserrat:wght@400;600&display=swap">
<style>
  :root {
    --backdrop: #e4e4e2;
    --paper: #ffffff;
    --sage: #9ba781;
    --sand: #cdb593;
    --ink: #1d1d1b;
    --leaf: #5c8f2e;
    --footer-text: #f4f5ee;
    --footer-faint: rgba(255,255,255,0.28);
  }
  * { box-sizing: border-box; margin: 0; padding: 0; }
  html, body {
    width: 1200px; height: 720px; overflow: hidden;
    background: var(--backdrop);
    font-family: "Montserrat", sans-serif;
  }
  .letterhead {
    position: absolute; left: 337px; top: 20px;
    width: 526px; height: 680px;
    background: var(--paper);
    box-shadow: 0 6px 24px rgba(0,0,0,0.12);
    overflow: hidden;
  }
  .brand {
    position: absolute; top: 26px; left: 0; right: 0;
    display: flex; flex-direction: column; align-items: center; gap: 6px;
  }
  .brand-dot {
    width: 34px; height: 34px; border-radius: 50%;
    background: var(--leaf);
  }
  .brand-name {
    font-size: 9px; font-weight: 600; letter-spacing: 1.5px;
    text-transform: uppercase; color: var(--ink);
  }
  .footer {
    position: absolute; left: 0; bottom: 0;
    width: 526px; height: 172px;
  }
  .footer-wave { position: absolute; inset: 0; }
  .footer-rule {
    position: absolute; left: 18px; top: 64px;
    width: 216px; height: 1px; background: var(--footer-faint);
  }
  .footer-address {
    position: absolute; left: 18px; top: 74px;
    font-size: 7.5px; line-height: 1.55; color: var(--footer-text);
  }
  .footer-contact {
    position: absolute; left: 180px; top: 78px;
    display: flex; flex-direction: column; gap: 10px;
    font-size: 7.5px; color: var(--footer-text);
  }
  .contact-row { display: flex; align-items: center; gap: 7px; }
  .contact-row svg { flex: none; }
  .footer-seal {
    position: absolute; right: 22px; top: 70px;
    width: 62px; height: 62px; border-radius: 50%;
    border: 1px solid var(--footer-faint);
    display: flex; align-items: center; justify-content: center;
    text-align: center;
    font-size: 6px; font-weight: 600; letter-spacing: 0.8px;
    text-transform: uppercase; color: var(--footer-faint);
    line-height: 1.4;
  }
</style>
</head>
<body>
  <main class="letterhead">
    <header class="brand">
      <span class="brand-dot"></span>
      <span class="brand-name">Wexford Tiller Holdings</span>
    </header>

    <footer class="footer">
      <svg class="footer-wave" width="526" height="172" viewBox="0 0 526 172" aria-hidden="true">
        <path d="M0 20 C120 0 210 4 300 32 C370 52 440 54 526 44 L526 172 L0 172 Z" fill="var(--sand)"/>
        <path d="M0 24 C110 14 200 20 290 40 C370 58 450 56 526 46 L526 172 L0 172 Z" fill="var(--sage)"/>
      </svg>
      <div class="footer-rule"></div>
      <address class="footer-address" style="font-style:normal">
        Wexford Tiller Holdings,<br>LLC.<br>PO Box 4410 Larkmont,<br>North Dakota 58990
      </address>
      <div class="footer-contact">
        <div class="contact-row">
          <svg width="7" height="11" viewBox="0 0 7 11" aria-hidden="true"><rect x="0.5" y="0.5" width="6" height="10" rx="1" fill="none" stroke="var(--footer-text)" stroke-width="0.8"/><line x1="2.5" y1="9" x2="4.5" y2="9" stroke="var(--footer-text)" stroke-width="0.8"/></svg>
          <span>(555) 310.4827</span>
        </div>
        <div class="contact-row">
          <svg width="10" height="7" viewBox="0 0 10 7" aria-hidden="true"><rect x="0.5" y="0.5" width="9" height="6" fill="none" stroke="var(--footer-text)" stroke-width="0.8"/><path d="M0.5 0.5 L5 4 L9.5 0.5" fill="none" stroke="var(--footer-text)" stroke-width="0.8"/></svg>
          <span>reception@tqvanholt.com</span>
        </div>
      </div>
      <div class="footer-seal">Wexford<br>Tiller<br>Holdings</div>
    </footer>
  </main>
</body>
</html>
```